Business Card for Personal Trainer company Vigor Crestline
Company name: Vigor Crestline
Business Card for Personal Trainer company Vigor Crestline - Health
Creative Brief
Simple
Owen Thistlecombe CPT
Body Transformation Expert
No address
info@vigorcrestline.co.uk
www.vigorcrestline.co.uk
On the front, can you put the logo in the middle and underneath the logo can you make my web address stand out. At the bottom, can you put my name and title and my contact details as icons. I want my phone number, email address, facebook fan page and twitter account as icons. For example, my phone as a little icon of a phone, my email address as a little unread email, facebook icon (vigcrest) and twitter icon (vig_crest). At the bottom where my phone number, email address, facebook and twitter accounts are going. Can you put them so it is my phone number, then to the right, my email address and underneath them, my facebook and to the right of facebook, my twitter account.
On the back of the card can you put: "Call today for a FREE body analysis and consultation or visit VigorCrestline.co.uk for your FREE Swift Lean Shift report". I will upload a money back guarantee image, please can you put that on the back, stating "results guaranteed or your money back".

```html
<!DOCTYPE html>
<html lang="en">
<head>
<meta charset="utf-8">
<title>Vigor Crestline – Business Card</title>
<link rel="stylesheet" href="https://fonts.googleapis.com/css2?family=Open+Sans:ital,wght@0,400;0,600;0,700;0,800;1,700&display=swap">
<style>
  :root {
    --backdrop: #d9dcdf;
    --card-top: #ffffff;
    --card-bottom: #e9ebed;
    --navy: #0f3a6b;
    --brand-blue: #1f5c9c;
    --band-blue: #2d72b8;
    --ink: #2b2f33;
    --ink-soft: #4a5056;
    --seal-blue: #2a64a8;
    --seal-rim: #b9c9dc;
  }
  * { box-sizing: border-box; margin: 0; padding: 0; }
  html, body { width: 1200px; height: 901px; overflow: hidden; }
  body {
    background: var(--backdrop);
    font-family: "Open Sans", Arial, sans-serif;
    color: var(--ink);
    position: relative;
  }
  .card {
    position: absolute;
    left: 260px;
    width: 680px;
    height: 389px;
    border-radius: 26px;
    background: linear-gradient(180deg, var(--card-top) 0%, var(--card-bottom) 100%);
    box-shadow: 0 2px 8px rgba(0,0,0,.12);
    overflow: hidden;
  }
  .card--back { top: 41px; }
  .card--front { top: 470px; }

  /* Back side */
  .offer {
    position: absolute;
    top: 44px; left: 40px; right: 40px;
    text-align: center;
    font-size: 17px;
    line-height: 1.45;
    color: var(--ink);
  }
  .offer__link { color: var(--brand-blue); font-weight: 700; text-decoration: underline; }
  .guarantee-seal {
    position: absolute;
    left: 50%; top: 150px;
    width: 170px; height: 170px;
    margin-left: -85px;
  }

  /* Front side */
  .brand {
    position: absolute;
    top: 78px; left: 0; right: 0;
    display: flex; align-items: center; justify-content: center; gap: 16px;
  }
  .brand__dot {
    width: 54px; height: 54px; border-radius: 50%;
    background: var(--brand-blue);
  }
  .brand__name {
    font-size: 44px; font-weight: 800; letter-spacing: 1px;
    color: var(--brand-blue); text-transform: uppercase;
  }
  .web-band {
    position: absolute; left: 0; right: 0; top: 196px; height: 28px;
  }
  .web-band__rule {
    position: absolute; left: 0; right: 0; top: 11px; height: 6px;
    background: var(--navy);
  }
  .web-band__bar {
    position: absolute; left: 250px; right: 0; top: 0; height: 28px;
    background: linear-gradient(180deg, var(--band-blue), var(--navy));
    color: #fff; font-style: italic; font-weight: 700; font-size: 18px;
    letter-spacing: 1.5px; line-height: 28px; padding-left: 18px;
  }
  .trainer {
    position: absolute; left: 300px; top: 234px;
  }
  .trainer__name { font-size: 22px; font-weight: 700; color: var(--brand-blue); line-height: 1.2; }
  .trainer__title { font-size: 15px; color: var(--ink-soft); }
  .contact {
    position: absolute; list-style: none; font-size: 15px; color: var(--ink-soft);
  }
  .contact li { display: flex; align-items: center; gap: 9px; height: 27px; }
  .contact--direct { left: 30px; top: 296px; }
  .contact--social { left: 548px; top: 308px; }
  .contact svg { width: 18px; height: 18px; fill: var(--navy); }
  .social-square { width: 16px; height: 16px; background: var(--navy); border-radius: 2px; }
</style>
</head>
<body>

<section class="card card--back" aria-label="Card back">
  <p class="offer">
    “Call today for a FREE body analysis and consultation<br>
    or visit <span class="offer__link">VigorCrestline.co.uk</span> for your FREE Swift Lean Shift report”
  </p>
  <svg class="guarantee-seal" viewBox="0 0 170 170" role="img" aria-label="Results guaranteed or your money back seal">
    <circle cx="85" cy="85" r="82" fill="var(--seal-rim)"/>
    <circle cx="85" cy="85" r="68" fill="var(--seal-blue)"/>
  </svg>
</section>

<section class="card card--front" aria-label="Card front">
  <div class="brand">
    <span class="brand__dot"></span>
    <span class="brand__name">Vigor Crestline</span>
  </div>

  <div class="web-band">
    <div class="web-band__rule"></div>
    <div class="web-band__bar">www.vigorcrestline.co.uk</div>
  </div>

  <div class="trainer">
    <p class="trainer__name">Owen Thistlecombe CPT</p>
    <p class="trainer__title">Body Transformation Expert</p>
  </div>

  <ul class="contact contact--direct">
    <li>
      <svg viewBox="0 0 24 24" aria-hidden="true"><path d="M6.6 10.8a15.1 15.1 0 0 0 6.6 6.6l2.2-2.2c.3-.3.7-.4 1-.2 1.1.4 2.3.6 3.6.6.6 0 1 .4 1 1V20c0 .6-.4 1-1 1A17 17 0 0 1 3 4c0-.6.4-1 1-1h3.5c.6 0 1 .4 1 1 0 1.3.2 2.5.6 3.6.1.3 0 .7-.2 1z"/></svg>
      01632 960 481
    </li>
    <li>
      <svg viewBox="0 0 24 24" aria-hidden="true"><path d="M3 5h18c.6 0 1 .4 1 1v12c0 .6-.4 1-1 1H3c-.6 0-1-.4-1-1V6c0-.6.4-1 1-1zm1 2.2V17h16V7.2l-8 5.3z M4.8 7 12 11.8 19.2 7z"/></svg>
      info@vigorcrestline.co.uk
    </li>
  </ul>

  <ul class="contact contact--social">
    <li><span class="social-square"></span>vigcrest</li>
    <li><span class="social-square"></span>vig_crest</li>
  </ul>
</section>

</body>
</html>
```